Utah Iron Ridge Marketing Flyer

I need a 1 page flyer that will go in a magazine to advertise our youth sports club and the various sports we have teams for. I want to make sure we feature pictures of our teams, our logos for basketball and volleyball, our title logo from our website and most importantly, HOW TO CONTACT US by going to our website www.utahironridge.example

Target Market(s)

Youth Sports Club

Colors
85cae6

Requirements
Must have
• Use the colors from our website: Carolina blue, black and silver. Must use the info provided in the Word Document I provided. Must have in bold and enlarged lettering how to contact us by going to our website www.utahironridge.example

```html
<!DOCTYPE html>
<html lang="en">
<head>
<meta charset="UTF-8">
<title>Utah Iron Ridge – Youth Sports Flyer</title>
<link href="https://fonts.googleapis.com/css2?family=Roboto:wght@300;400;500;700;900&family=Lato:wght@400;700;900&display=swap" rel="stylesheet">
<style>
  :root {
    --carolina: #85cae6;
    --ink: #05070d;
    --navy: #0b1a33;
    --deep-blue: #12386e;
    --glow: #3f8fe0;
    --white: #ffffff;
    --silver: #c9d2dc;
    --page: #e6e6e6;
    --band: rgba(8, 12, 22, 0.88);
  }
  * { margin: 0; padding: 0; box-sizing: border-box; }
  html, body { width: 1200px; height: 900px; overflow: hidden; }
  body { background: var(--page); font-family: "Roboto", sans-serif; position: relative; }

  .flyer {
    position: absolute; left: 296px; top: 20px;
    width: 608px; height: 860px; overflow: hidden;
    background: linear-gradient(180deg, var(--ink) 0%, var(--navy) 35%, var(--deep-blue) 70%, #0e2c57 100%);
    color: var(--white);
  }

  .arena-photo {
    position: absolute; left: 0; top: 300px; width: 608px; height: 560px;
    background:
      radial-gradient(circle at 36% 52%, #e0782c 0 24%, transparent 24.3%),
      radial-gradient(ellipse at 30% 25%, rgba(170,215,255,0.75) 0 6%, transparent 28%),
      radial-gradient(ellipse at 85% 55%, rgba(150,205,255,0.6) 0 5%, transparent 30%),
      radial-gradient(ellipse at 50% 50%, rgba(63,143,224,0.5) 0%, transparent 70%);
  }

  .headline { position: absolute; left: 40px; top: 40px; line-height: 1; }
  .headline .lead { font-size: 38px; font-weight: 400; letter-spacing: 0.5px; }
  .headline .sports {
    font-family: "Lato", sans-serif; font-weight: 900; color: var(--carolina);
    font-size: 38px; letter-spacing: 1px; line-height: 1.0; margin-top: 4px;
  }
  .headline .amp { color: var(--white); }
  .headline .tail { font-size: 36px; font-weight: 400; line-height: 1.05; margin-top: 6px; }

  .brand {
    position: absolute; right: 40px; top: 120px;
    display: flex; align-items: center; gap: 10px;
  }
  .brand-dot { width: 22px; height: 22px; border-radius: 50%; background: var(--carolina); }
  .brand-name { font-family: "Lato", sans-serif; font-weight: 900; font-size: 26px; color: var(--carolina); }

  .details { position: absolute; left: 390px; top: 300px; width: 190px; }
  .audience { font-family: "Lato", sans-serif; font-weight: 900; font-size: 17px; letter-spacing: 0.5px; }
  .grades { font-size: 16px; font-weight: 400; margin-bottom: 18px; }
  .tryout { border-top: 1px solid var(--silver); padding-top: 4px; margin-bottom: 20px; }
  .tryout-sport { font-size: 15px; font-weight: 300; border-bottom: 1px solid var(--silver); padding-bottom: 3px; }
  .tryout-when { font-family: "Lato", sans-serif; font-weight: 900; font-size: 14px; text-transform: uppercase; line-height: 1.2; margin-top: 3px; }
  .teams { font-size: 14px; font-weight: 300; line-height: 1.3; margin-top: 6px; }

  .contact-band {
    position: absolute; left: 0; bottom: 0; width: 608px; height: 120px;
    background: var(--band);
  }
  .website { position: absolute; left: 36px; top: 22px; }
  .website-label { font-size: 13px; font-weight: 400; }
  .website-url { font-family: "Lato", sans-serif; font-weight: 900; font-size: 24px; margin-top: 4px; }
  .admin { position: absolute; right: 36px; bottom: 22px; text-align: left; }
  .admin-role { font-size: 13px; font-weight: 400; }
  .admin-phone { font-family: "Lato", sans-serif; font-weight: 900; font-size: 19px; display: flex; align-items: center; gap: 6px; margin-top: 3px; }
</style>
</head>
<body>
  <main class="flyer">
    <div class="arena-photo" role="img" aria-label="Basketball in front of a stadium lit by bright arena lights, resting on a hoop"></div>

    <header class="headline">
      <div class="lead">UTAH BASED</div>
      <div class="sports">BASKETBALL<br>VOLLEYBALL<br><span class="amp">&amp;</span> SOFTBALL</div>
      <div class="tail">Club youth sports<br>program</div>
    </header>

    <div class="brand">
      <span class="brand-dot"></span>
      <span class="brand-name">Utah Iron Ridge</span>
    </div>

    <section class="details">
      <div class="audience">BOYS AND GIRLS</div>
      <div class="grades">2nd – 12th grades</div>

      <div class="tryout">
        <div class="tryout-sport">Basketball Tryouts</div>
        <div class="tryout-when">End of August</div>
      </div>
      <div class="tryout">
        <div class="tryout-sport">Volleyball Tryouts</div>
        <div class="tryout-when">October for Jr. High<br>November for High School</div>
      </div>
      <div class="tryout">
        <div class="tryout-sport">Softball Tryouts</div>
        <div class="tryout-when">July</div>
      </div>

      <p class="teams">Teams range from Developmental to Premier Travel teams, so if you're looking to improve your skills, we can help.</p>
    </section>

    <footer class="contact-band">
      <div class="website">
        <div class="website-label">For more information visit our website:</div>
        <div class="website-url">www.utahironridge.example</div>
      </div>
      <div class="admin">
        <div class="admin-role">Club Administrator</div>
        <div class="admin-phone">
          <svg width="14" height="14" viewBox="0 0 24 24" aria-hidden="true"><path fill="#fff" d="M6.6 10.8a15 15 0 0 0 6.6 6.6l2.2-2.2a1 1 0 0 1 1-.25 11.4 11.4 0 0 0 3.6.57 1 1 0 0 1 1 1V20a1 1 0 0 1-1 1A17 17 0 0 1 3 4a1 1 0 0 1 1-1h3.5a1 1 0 0 1 1 1c0 1.25.2 2.45.57 3.6a1 1 0 0 1-.25 1z"/></svg>
          801-555-0147
        </div>
      </div>
    </footer>
  </main>
</body>
</html>
```